harvest Soon Book Cover Design for real estate investment book

I am looking for a Book Cover design for my new book. I would like designs for a hardcover, softcover and Lumora book.

The book deals with real estate and mortgage investments. Looking for a clean, bright simple design. Want to cover to be White with big RED letters. See "Dancing past Noon" book for an example ... see attached.

Target Market(s)

Affluent people with money looking for investment solutions.

Industry/Entity Type

Financial Service

Font styles to use
Serif

Requirements
Must have
• Bright clean design that will be appealing to affluent people.
• Title: harvest SOON
• Subtitle: A quiet method for thriving through land holdings
• subsubtitle: Secrets the Bank Teller Keeps Hidden From Clients...
• Author: Ned Falconby
• My Picture on the inside cover or on the back cover
• Book Description, Author description
Nice to have
• Focus on the Front cover look and feel first. Then we can look at the inside flaps and back cover. I will need to send you text. This is for the full cover. Front. Back. Spine. Inside flaps fro hardcover.

```html
<!DOCTYPE html>
<html lang="en">
<head>
<meta charset="utf-8">
<title>harvest SOON — Ned Falconby</title>
<link rel="stylesheet" href="https://fonts.googleapis.com/css2?family=Oranienbaum&family=Cinzel:wght@400;500&family=Crimson+Text&display=swap">
<style>
  :root {
    --paper: #ffffff;
    --band: #f1f1f1;
    --title-red: #ee2316;
    --ink: #111111;
  }
  html, body {
    margin: 0;
    padding: 0;
    overflow: hidden;
    background: var(--paper);
  }
  .book-cover {
    position: relative;
    width: 800px;
    height: 1200px;
    background: var(--paper);
    overflow: hidden;
  }
  .teaser-band {
    position: absolute;
    top: 0;
    left: 0;
    width: 800px;
    height: 92px;
    background: var(--band);
    display: flex;
    align-items: center;
    justify-content: center;
  }
  .teaser-band p {
    margin: 0;
    font-family: "Crimson Text", Georgia, serif;
    font-size: 25px;
    color: var(--ink);
    letter-spacing: 0.2px;
  }
  .cover-type {
    position: absolute;
    top: 0;
    left: 0;
  }
  .title-word {
    font-family: "Oranienbaum", "Bodoni Moda", serif;
    fill: var(--title-red);
  }
  .subtitle-line,
  .author-name {
    font-family: "Cinzel", "Trajan Pro", serif;
    fill: var(--ink);
  }
</style>
</head>
<body>
  <main class="book-cover">
    <header class="teaser-band">
      <p>Secrets the Bank Teller Keeps Hidden From Clients...</p>
    </header>

    <svg class="cover-type" width="800" height="1200" viewBox="0 0 800 1200" xmlns="http://www.w3.org/2000/svg">
      <g class="title">
        <text class="title-word title-word--top" x="49" y="410" font-size="345"
              textLength="711" lengthAdjust="spacingAndGlyphs">harvest</text>
        <text class="title-word title-word--bottom" x="49" y="819" font-size="540"
              textLength="711" lengthAdjust="spacingAndGlyphs">SOON</text>
      </g>

      <g class="subtitle">
        <text class="subtitle-line" x="400" y="905" font-size="46" text-anchor="middle"
              textLength="660" lengthAdjust="spacingAndGlyphs">A quiet method for thriving</text>
        <text class="subtitle-line" x="400" y="959" font-size="46" text-anchor="middle"
              textLength="620" lengthAdjust="spacingAndGlyphs">through land holdings</text>
      </g>

      <text class="author-name" x="400" y="1136" font-size="92" text-anchor="middle"
            textLength="610" lengthAdjust="spacingAndGlyphs">Ned Falconby</text>
    </svg>
  </main>
</body>
</html>
```